OKU professional cleaner

this professional multi-surface cleaner is intended for professionals.
Powerful degreaser. We would like to focus on the professional side.
We already have a range of disinfectants, and we would like a design close to this range but still distinct. The name is OKU and yhe logo is NUVAShine.the visible part of the label is 55mm and will be affixed to a round bottle with trigger .

Target Market(s)

professional

```html
<!DOCTYPE html>
<html lang="en">
<head>
<meta charset="utf-8">
<title>OKU Powerful Degreaser – Label Colourways</title>
<link href="https://fonts.googleapis.com/css2?family=Bebas+Neue&family=Roboto:wght@400;500;700&family=Roboto+Condensed:wght@400&display=swap" rel="stylesheet">
<style>
  :root {
    --page-bg: #f6f6f6;
    --ink-dark: #383838;
    --ink-red: #c4161e;
    --ink-maroon: #5a2629;
    --ink-body: #2c2c2c;
    --brand-green: #72b35a;
    --rule: #2e2a2a;
    --label-base: #ececec;
    --blue-top: #4f9fc8;
    --blue-mid: #c9dfea;
    --amber-top: #cf8124;
    --amber-mid: #efd9bd;
    --flag-black: #2f2f2f;
    --flag-yellow: #f2dc4a;
    --flag-red: #c6454b;
  }
  * { box-sizing: border-box; margin: 0; padding: 0; }
  html, body {
    width: 1200px; height: 1200px; overflow: hidden;
    background: var(--page-bg);
  }
  .sheet {
    position: relative; width: 1200px; height: 1200px;
    display: flex; justify-content: center; align-items: center; gap: 60px;
  }
  .label {
    position: relative; width: 480px; height: 850px; overflow: hidden;
    background: var(--label-base);
    box-shadow: 0 2px 10px rgba(0,0,0,0.08);
  }
  .label--blue {
    background:
      radial-gradient(ellipse 60% 30% at 85% 0%, rgba(40,130,180,0.55), transparent 70%),
      linear-gradient(180deg, var(--blue-top) 0%, #9cc5dc 22%, var(--blue-mid) 40%, #e8eef2 58%, var(--label-base) 80%);
  }
  .label--amber {
    background:
      radial-gradient(ellipse 60% 30% at 70% 0%, rgba(195,110,20,0.6), transparent 70%),
      linear-gradient(180deg, var(--amber-top) 0%, #e2ad6e 22%, var(--amber-mid) 40%, #f2ebe2 58%, var(--label-base) 80%);
  }
  .brand {
    position: absolute; left: 56px; top: 158px;
    font-family: "Roboto", sans-serif; font-weight: 500;
    font-size: 42px; line-height: 1; color: var(--brand-green); letter-spacing: 0.5px;
  }
  .headline {
    position: absolute; left: 56px; overflow: visible;
    font-family: "Bebas Neue", sans-serif;
  }
  .headline--top { top: 284px; }
  .headline--top text { fill: var(--ink-dark); font-size: 76px; }
  .headline--main { top: 368px; }
  .headline--main text { fill: var(--ink-red); font-size: 120px; }
  .rule {
    position: absolute; left: 56px; width: 392px; height: 3px;
    background: var(--rule);
  }
  .rule--upper { top: 514px; }
  .rule--lower { top: 752px; left: 52px; }
  .audience {
    position: absolute; left: 56px; top: 533px;
    font-family: "Roboto", sans-serif; font-weight: 700; font-size: 36px; line-height: 1;
    color: var(--ink-maroon);
  }
  .descriptor {
    position: absolute; left: 56px; top: 580px;
    font-family: "Roboto", sans-serif; font-weight: 400; font-size: 37px; line-height: 1;
    color: var(--ink-body);
  }
  .origin {
    position: absolute; left: 56px; top: 652px;
    font-family: "Roboto Condensed", sans-serif; font-size: 24px; line-height: 1;
    color: var(--ink-body);
  }
  .flag { position: absolute; left: 56px; top: 685px; }
  .volume {
    position: absolute; left: 54px; top: 778px;
    font-family: "Roboto Condensed", sans-serif; font-size: 26px; line-height: 1;
    color: var(--ink-body);
  }
</style>
</head>
<body>
<main class="sheet">
  <section class="label label--blue">
    <div class="brand">NUVAShine</div>
    <svg class="headline headline--top" width="230" height="70" viewBox="0 0 230 70">
      <text x="0" y="62" textLength="228" lengthAdjust="spacingAndGlyphs">POWERFUL</text>
    </svg>
    <svg class="headline headline--main" width="392" height="100" viewBox="0 0 392 100">
      <text x="0" y="92" textLength="390" lengthAdjust="spacingAndGlyphs">DEGREASER</text>
    </svg>
    <div class="rule rule--upper"></div>
    <div class="audience">PROFESSIONAL</div>
    <div class="descriptor">multi-surface cleaner</div>
    <div class="origin">made in</div>
    <svg class="flag" width="76" height="44" viewBox="0 0 76 44" aria-label="Belgian flag">
      <rect x="0" y="0" width="25.4" height="44" fill="var(--flag-black)"/>
      <rect x="25.3" y="0" width="25.4" height="44" fill="var(--flag-yellow)"/>
      <rect x="50.6" y="0" width="25.4" height="44" fill="var(--flag-red)"/>
    </svg>
    <div class="rule rule--lower"></div>
    <div class="volume">Net.Wt. 750 ml</div>
  </section>

  <section class="label label--amber">
    <div class="brand">NUVAShine</div>
    <svg class="headline headline--top" width="230" height="70" viewBox="0 0 230 70">
      <text x="0" y="62" textLength="228" lengthAdjust="spacingAndGlyphs">POWERFUL</text>
    </svg>
    <svg class="headline headline--main" width="392" height="100" viewBox="0 0 392 100">
      <text x="0" y="92" textLength="390" lengthAdjust="spacingAndGlyphs">DEGREASER</text>
    </svg>
    <div class="rule rule--upper"></div>
    <div class="audience">PROFESSIONAL</div>
    <div class="descriptor">multi-surface cleaner</div>
    <div class="origin">made in</div>
    <svg class="flag" width="76" height="44" viewBox="0 0 76 44" aria-label="Belgian flag">
      <rect x="0" y="0" width="25.4" height="44" fill="var(--flag-black)"/>
      <rect x="25.3" y="0" width="25.4" height="44" fill="var(--flag-yellow)"/>
      <rect x="50.6" y="0" width="25.4" height="44" fill="var(--flag-red)"/>
    </svg>
    <div class="rule rule--lower"></div>
    <div class="volume">Net.Wt. 750 ml</div>
  </section>
</main>
</body>
</html>
```